Private Gym Needs a Rack Card Design

We need a basic front and back rack card (same size as post card) that gives basic information about our brand, and includes our logo. Please see attached logo and required content below.

Target Market(s)

Upscale, private gym.

Industry/Entity Type

Gym

Font styles to use
Sans Serif

Colors
ffffff
5c5c5c
000000
dbdbdb
f78f20

Requirements
Must have
• Business Logo and the following text in a clean, modern, easy-to-read, artistic manner. Style and design must be clean, incorporate our color scheme of MOSTLY white, light grey, charcoal, with just pops of orange. We want the card itself to be mostly white background. Must include website URL as well: corevantagestudio.com
• FRONT CARD:
• Logo
• A safe and individualized approach to exercise
• Our method employs the latest weight resistance training exercises and coaching for healthy living. Not only is our workout methodology effective, it’s safe.
• Our Method…
• -Improves Functional Movement
• -Promotes Weight Loss
• -Builds Strength
• -Increases Flexibility 

• BACK:
• Change Your Body. Find Your Strength.
• There’s 40 years of success behind our proven method
• What is The Formwell? 
• The Formwell is all about teaching our clients how to lift weights and exercise with the proper technique. There’s no slinging or jerking at our gym; only controlled movements that yield real results.
• Come workout with us in our private gym. We are located in Durham adjacent to Harlow Campus and 5 minutes from downtown Durham.
• Address: 482 Linden Ave, Durham, NC 27705
• Phone: (919) 555-2741
• Hours: 9:00 AM – 9:00 PM
Nice to have
• Great organization of text, maybe some columns, colored bullet points, cool graphics and logos.
Should not have
• Busy or crowded design. All lines should be sleek, straight, and streamline. NO STOCK IMAGES, but logos are GREAT

```html
<!DOCTYPE html>
<html lang="en">
<head>
<meta charset="utf-8">
<title>The Formwell – Rack Card</title>
<link rel="stylesheet" href="https://fonts.googleapis.com/css2?family=Questrial&family=Open+Sans:ital,wght@0,400;1,700&family=Roboto+Condensed:ital,wght@0,400;0,700;1,400;1,700&display=swap">
<style>
  :root{
    --orange:#ee6436;
    --orange-soft:#f4896a;
    --charcoal:#4a4a4a;
    --band:#3d3d3d;
    --text:#5c5c5c;
    --rule:#dbdbdb;
    --white:#ffffff;
    --stage:#ececec;
    --strip:#ededed;
  }
  *{box-sizing:border-box;margin:0;padding:0}
  html,body{width:928px;height:1200px;overflow:hidden}
  body{background:var(--stage);position:relative;font-family:"Open Sans",sans-serif;color:var(--text)}
  .card{position:absolute;left:118px;width:671px;height:438px;background:var(--white);overflow:hidden;box-shadow:0 2px 10px rgba(0,0,0,.12)}
  .card--front{top:111px}
  .card--back{top:626px}
  .card__art{position:absolute;left:0;top:0}
  .brand{position:absolute;left:20px;top:50px;font-family:"Questrial",sans-serif;font-size:34px;color:var(--charcoal);display:flex;align-items:center;gap:8px;letter-spacing:.5px}
  .brand__mark{width:14px;height:14px;background:var(--orange)}
  .tagline{position:absolute;left:21px;top:144px;font-family:"Questrial",sans-serif;font-size:20px;line-height:27px;color:var(--white)}
  .tagline b{color:var(--orange);font-weight:700}
  .tagline--back{left:21px;top:145px;font-size:20px;line-height:26px}
  .tagline--back .indent{padding-left:57px}
  .label{position:absolute;display:flex;align-items:center;height:20px;background:var(--band);color:var(--white);font-weight:700;clip-path:polygon(0 0,100% 0,calc(100% - 14px) 100%,0 100%)}
  .label::after{content:"";position:absolute;right:-3px;top:0;width:12px;height:20px;background:var(--orange);clip-path:polygon(0 0,40% 0,100% 100%,60% 100%)}
  .label--method{left:34px;top:266px;width:154px;padding-left:7px;font-family:"Open Sans",sans-serif;font-size:15.5px;letter-spacing:.4px}
  .label--what{left:26px;top:262px;width:206px;padding-left:6px;font-family:"Roboto Condensed",sans-serif;font-size:16px}
  .benefits{position:absolute;left:44px;top:293px;list-style:none;font-family:"Questrial",sans-serif;font-size:17px;color:var(--text)}
  .benefits li{display:flex;align-items:center;gap:11px;height:24.7px}
  .benefits li::before{content:"";flex:none;width:8px;height:8px;border-radius:50%;background:var(--orange);box-shadow:0 0 0 3px var(--white),0 0 0 4.5px var(--orange);margin:0 3px}
  .divider{position:absolute;width:1px;background:linear-gradient(transparent,#bdbdbd,transparent)}
  .divider--front{left:349px;top:253px;height:130px}
  .divider--back{left:369px;top:261px;height:113px}
  .summary{position:absolute;left:377px;top:273px;width:266px;font-size:14.3px;letter-spacing:-.15px;line-height:18.4px;text-align:justify;text-align-last:justify;color:var(--text)}
  .summary em{display:block;text-align-last:left;color:var(--orange);font-weight:700}
  .footbar{position:absolute;right:0;top:401px;height:37px;width:320px;background:var(--orange);clip-path:polygon(20px 0,100% 0,100% 100%,0 100%);color:var(--white);display:flex;align-items:center}
  .footbar--url{font-size:19px;padding-left:36px}
  .footbar--phone{font-family:"Roboto Condensed",sans-serif;font-weight:700;font-size:23px;padding-left:50px;gap:7px}
  .proof{position:absolute;left:324px;top:226px;width:347px;height:27px;background:var(--strip);clip-path:polygon(8px 0,100% 0,100% 100%,0 100%);font-family:"Roboto Condensed",sans-serif;font-style:italic;font-size:13.5px;color:var(--text);display:flex;align-items:center;padding-left:16px}
  .proof b{font-weight:700;color:var(--charcoal)}
  .about{position:absolute;left:27px;top:286px;width:314px;font-family:"Roboto Condensed",sans-serif;font-size:14.6px;line-height:17.5px;text-align:justify;color:#333}
  .visit{position:absolute;left:401px;top:283px;width:245px;font-size:12.6px;letter-spacing:-.1px;line-height:16.4px;text-align:justify;color:#333}
  .visit em{color:var(--orange);font-weight:700}
  .hours{position:absolute;left:401px;top:364px;width:190px;font-family:"Roboto Condensed",sans-serif;font-size:16px;color:#333;border-bottom:1px solid var(--rule);padding-bottom:1px}
  .hours b{color:var(--orange)}
  .address{position:absolute;left:40px;top:408px;font-family:"Roboto Condensed",sans-serif;font-size:18px;color:#333;display:flex;align-items:center;gap:6px}
</style>
</head>
<body>

<section class="card card--front">
  <svg class="card__art" width="671" height="224" viewBox="0 0 671 224">
    <polygon points="292,0 671,0 671,224 410,224" fill="#c9b9ae" role="img" aria-label="Photo area: women stretching on mats in a bright studio"/>
    <polygon points="229,0 268,0 392,224 352,224" fill="var(--orange)" opacity=".85"/>
    <polygon points="262,0 300,0 420,224 382,224" fill="var(--orange-soft)" opacity=".7"/>
    <polygon points="300,0 320,0 440,224 420,224" fill="var(--orange-soft)" opacity=".4"/>
    <polygon points="0,141 272,141 309,204 0,204" fill="var(--band)"/>
  </svg>
  <div class="brand"><span class="brand__mark"></span>The Formwell</div>
  <p class="tagline">A <b>safe</b> and <b>individualized</b><br>approach to <b>exercise</b></p>

  <div class="label label--method">OUR METHOD</div>
  <ul class="benefits">
    <li>Improves Functional Movement</li>
    <li>Promotes Weight Loss</li>
    <li>Builds Strength</li>
    <li>Increases Flexibility</li>
  </ul>
  <div class="divider divider--front"></div>
  <p class="summary">Our method employs the latest weight resistance training exercises and coaching for healthy living. Not only is our workout methodology effective, <em>it’s safe.</em></p>
  <div class="footbar footbar--url">www.corevantagestudio.com</div>
</section>

<section class="card card--back">
  <svg class="card__art" width="671" height="224" viewBox="0 0 671 224">
    <polygon points="292,0 671,0 671,222 410,222" fill="#c8cdd2" role="img" aria-label="Photo area: man and woman smiling on exercise bikes in a bright gym"/>
    <polygon points="229,0 268,0 392,222 352,222" fill="var(--orange)" opacity=".85"/>
    <polygon points="262,0 300,0 420,222 382,222" fill="var(--orange-soft)" opacity=".7"/>
    <polygon points="300,0 320,0 440,222 420,222" fill="var(--orange-soft)" opacity=".4"/>
    <polygon points="0,141 272,141 309,203 0,203" fill="var(--band)"/>
  </svg>
  <div class="brand"><span class="brand__mark"></span>The Formwell</div>
  <p class="tagline tagline--back">Change Your <b>Body.</b><br><span class="indent">Find Your <b>Strength</b></span></p>
  <div class="proof">There’s&nbsp;<b>40 years of success</b>&nbsp;behind our proven method</div>

  <div class="label label--what">WHAT IS THE FORMWELL?</div>
  <p class="about">The Formwell is all about teaching our clients how to lift weights and exercise with the proper technique. There’s no slinging or jerking at our gym; only controlled movements that yield real results.</p>
  <div class="divider divider--back"></div>
  <p class="visit"><em>Come workout with us</em> in our private gym. We are located in Durham adjacent to Harlow Campus and 5 minutes from downtown Durham.</p>
  <p class="hours"><b>Hours:</b> 9:00 AM – 9:00 PM</p>

  <p class="address"><svg width="18" height="18" viewBox="0 0 18 18"><circle cx="9" cy="9" r="8" fill="none" stroke="var(--orange)" stroke-width="1.4"/><path d="M9 14s-3.3-3.6-3.3-6a3.3 3.3 0 0 1 6.6 0c0 2.4-3.3 6-3.3 6z" fill="var(--orange)"/><circle cx="9" cy="8" r="1.2" fill="var(--white)"/></svg>482 Linden Ave, Durham, NC 27705</p>
  <div class="footbar footbar--phone"><svg width="22" height="22" viewBox="0 0 22 22"><circle cx="11" cy="11" r="9.8" fill="none" stroke="var(--white)" stroke-width="1.6"/><path d="M7.6 6.2l2 2.1-1 1.3c.7 1.5 1.9 2.7 3.4 3.4l1.3-1 2.1 2-1 1.6c-3.7-.4-7.4-4.1-7.8-7.8z" fill="var(--white)"/></svg>(919) 555-2741</div>
</section>

</body>
</html>
```